Keystone Wiring LLC

I need a business card containing the following:

KeystoneWiringLLC
Certified Master Electrician
Licensed and insured
"powered by excellence"

Dale Brunholt. Owen Taliferro
484-215-6390 215-846-3027

KeystoneWiringLLC.com

red white and blue color scheme

Brief has been updated. colour scheme is included, tagline is changed thanks Added Wednesday, August 30, 2017

Industry/Entity Type

Electric Company

Contact Information for Business Card

Red white and blue coloring

Colors
ec1f27
0456a4
ffffff

Requirements
Must have
• Keystone Wiring
• Certified master Electrician
• Liscensed and insured
• "Powered by excellence"
• Dale Brunholt. 4842156390
• Owen Taliferro. 2158463027

```html
<!DOCTYPE html>
<html lang="en">
<head>
<meta charset="utf-8">
<title>Keystone Wiring — Business Cards</title>
<link rel="stylesheet" href="https://fonts.googleapis.com/css2?family=Exo+2:wght@600;800&family=Arimo:wght@400;700&display=swap">
<style>
  :root {
    --backdrop: #000000;
    --paper: #f7f7f7;
    --brand-red: #ec1f27;
    --brand-blue: #0456a4;
    --steel-light: #b3bbdf;
    --steel-mid: #8e9ccb;
    --caption-blue: #a9b3dc;
    --white: #ffffff;
  }
  * { box-sizing: border-box; margin: 0; padding: 0; }
  html, body {
    width: 1200px;
    height: 1000px;
    overflow: hidden;
    background: var(--backdrop);
  }
  .sheet { position: relative; width: 1200px; height: 1000px; }
  .card {
    position: absolute;
    left: 258px;
    width: 683px;
    height: 390px;
    background: var(--paper);
    overflow: hidden;
  }
  .card--first { top: 96px; }
  .card--second { top: 520px; }
  .card__stripes { position: absolute; inset: 0; width: 683px; height: 390px; }
  .wordmark {
    position: absolute;
    left: 25px;
    top: 20px;
    font-family: "Exo 2", sans-serif;
    font-weight: 800;
    font-size: 40px;
    line-height: 46px;
    letter-spacing: 1px;
    text-transform: uppercase;
    color: var(--brand-red);
  }
  .contact {
    position: absolute;
    left: 25px;
    top: 134px;
    font-family: "Arimo", sans-serif;
    color: var(--brand-red);
  }
  .contact__phone { font-weight: 700; font-size: 22px; line-height: 28px; }
  .contact__email { font-size: 17px; line-height: 24px; margin-top: 3px; }
  .holder {
    position: absolute;
    right: 25px;
    top: 232px;
    text-align: right;
  }
  .holder__name {
    font-family: "Exo 2", sans-serif;
    font-weight: 600;
    font-size: 28px;
    line-height: 36px;
    letter-spacing: 0.5px;
    color: var(--white);
  }
  .holder__credential {
    font-family: "Arimo", sans-serif;
    font-size: 19px;
    line-height: 27px;
    color: var(--caption-blue);
  }
  .holder__credential:first-of-type { margin-top: 4px; }
  .tagline {
    position: absolute;
    right: 25px;
    top: 344px;
    font-family: "Exo 2", sans-serif;
    font-weight: 600;
    font-style: italic;
    font-size: 21px;
    letter-spacing: 9px;
    margin-right: -9px;
    color: var(--white);
  }
</style>
</head>
<body>
<main class="sheet">

  <section class="card card--first">
    <svg class="card__stripes" viewBox="0 0 683 390" aria-hidden="true">
      <defs>
        <linearGradient id="steelBand1" x1="0" y1="1" x2="1" y2="0">
          <stop offset="0" stop-color="var(--steel-mid)"/>
          <stop offset="0.6" stop-color="var(--steel-light)"/>
          <stop offset="1" stop-color="var(--steel-mid)"/>
        </linearGradient>
      </defs>
      <polygon points="600,0 683,0 683,390 0,390" fill="url(#steelBand1)"/>
      <polygon points="683,0 683,390 0,390" fill="var(--brand-blue)"/>
      <polygon points="683,4 683,390 95,390" fill="var(--brand-red)"/>
    </svg>
    <div class="wordmark">Keystone<br>Wiring</div>
    <div class="contact">
      <p class="contact__phone">484-215-6390</p>
      <p class="contact__email">office@keystonewiringllc.com</p>
    </div>
    <div class="holder">
      <p class="holder__name">Dale Brunholt</p>
      <p class="holder__credential">Certified Master Electrician</p>
      <p class="holder__credential">Licensed and insured</p>
    </div>
    <p class="tagline">powered by excellence</p>
  </section>

  <section class="card card--second">
    <svg class="card__stripes" viewBox="0 0 683 390" aria-hidden="true">
      <defs>
        <linearGradient id="steelBand2" x1="0" y1="1" x2="1" y2="0">
          <stop offset="0" stop-color="var(--steel-mid)"/>
          <stop offset="0.6" stop-color="var(--steel-light)"/>
          <stop offset="1" stop-color="var(--steel-mid)"/>
        </linearGradient>
      </defs>
      <polygon points="600,0 683,0 683,390 0,390" fill="url(#steelBand2)"/>
      <polygon points="683,0 683,390 0,390" fill="var(--brand-blue)"/>
      <polygon points="683,4 683,390 95,390" fill="var(--brand-red)"/>
    </svg>
    <div class="wordmark">Keystone<br>Wiring</div>
    <div class="contact">
      <p class="contact__phone">215-846-3027</p>
      <p class="contact__email">office@keystonewiringllc.com</p>
    </div>
    <div class="holder">
      <p class="holder__name">Owen Taliferro</p>
      <p class="holder__credential">Certified Master Electrician</p>
      <p class="holder__credential">Licensed and insured</p>
    </div>
    <p class="tagline">powered by excellence</p>
  </section>

</main>
</body>
</html>
```